Business Card Design Quandong Celebration Crafters

on the front i would like to see the logo and my contact details. on the back i would like it to include the 3 parts to the business party planning, party hire and party supplies also with a line at the bottom (or white space) to write their appointment details.

Target Market(s)

mums and corporates

Industry/Entity Type

Business

Requirements
Must have
• logo and contact details which are: Name: Rosalind, Phone: 0417365920, email: ros@quandongfetes.com.au, Website: www.quandongfetes.com.au,

```html
<!DOCTYPE html>
<html lang="en">
<head>
<meta charset="utf-8">
<title>Quandong Celebration Crafters — Business Card</title>
<link rel="stylesheet" href="https://fonts.googleapis.com/css2?family=Lato:wght@400;700&display=swap">
<style>
  :root {
    --yellow: #f6bc25;
    --magenta: #bb4f9f;
    --cyan: #1fb2d3;
    --purple: #5a3e97;
    --paper: #ffffff;
    --rule: #cfcfcf;
    --backdrop: #e9e9ec;
    --text-on-band: #ffffff;
  }
  * { box-sizing: border-box; margin: 0; padding: 0; }
  html, body {
    width: 1200px; height: 926px; overflow: hidden;
    background: var(--backdrop);
    font-family: "Lato", Arial, sans-serif;
  }
  .canvas { position: relative; width: 1200px; height: 926px; }

  .card {
    position: absolute; left: 250px; width: 700px; height: 400px;
    background: var(--paper);
    box-shadow: 0 6px 18px rgba(0,0,0,.18);
    overflow: hidden;
  }
  .card--front { top: 50px; }
  .card--back { top: 476px; }

  /* Front: brand block */
  .brand { position: absolute; left: 40px; top: 90px; width: 270px; }
  .brand__illustration {
    width: 150px; height: 120px; margin-left: 60px;
    border-radius: 10px;
    background: linear-gradient(135deg, #a47a5c 0%, #c98fbf 55%, #7a5fc0 100%);
  }
  .brand__name {
    margin-top: 14px;
    font-weight: 700; font-size: 26px; line-height: 1.15;
    color: var(--cyan); text-align: center;
  }

  /* Front: name band */
  .name-band {
    position: absolute; left: 340px; right: 0; top: 58px; height: 50px;
    background: var(--magenta);
    color: var(--text-on-band);
    font-size: 28px; font-weight: 400;
    padding-left: 20px; line-height: 50px; letter-spacing: .5px;
  }

  /* Front: contact bands */
  .contact { position: absolute; left: 330px; right: 0; top: 262px; list-style: none; }
  .contact__item {
    height: 34px; margin-bottom: 2px;
    display: flex; align-items: center; gap: 12px;
    padding-left: 14px;
    color: var(--text-on-band); font-size: 19px;
  }
  .contact__item--phone { background: var(--yellow); }
  .contact__item--email { background: var(--cyan); }
  .contact__item--web { background: var(--purple); }
  .contact__icon { width: 18px; height: 18px; flex: none; }

  /* Bottom colour strip */
  .strip { position: absolute; left: 0; right: 0; bottom: 0; height: 8px; display: flex; }
  .strip span { flex: 1; }
  .strip .s-yellow { background: var(--yellow); }
  .strip .s-magenta { background: var(--magenta); }
  .strip .s-cyan { background: var(--cyan); }
  .strip .s-purple { background: var(--purple); }

  /* Back: services with writing lines */
  .services { position: absolute; left: 50px; right: 50px; top: 40px; }
  .service { position: relative; height: 80px; }
  .service__tag {
    position: absolute; left: 0; top: 0;
    height: 30px; line-height: 30px; padding: 0 14px;
    color: var(--text-on-band); font-size: 17px; font-weight: 700;
  }
  .service__tag--yellow { background: var(--yellow); }
  .service__tag--magenta { background: var(--magenta); }
  .service__tag--cyan { background: var(--cyan); }
  .service__rule { position: absolute; height: 1px; background: var(--rule); right: 0; }
  .service__rule--inline { top: 30px; }
  .service__rule--full { left: 0; top: 64px; }
  .appointment { position: absolute; left: 50px; right: 50px; top: 296px; }
  .appointment__rule { height: 1px; background: var(--rule); margin-bottom: 34px; }
</style>
</head>
<body>
<main class="canvas">

  <section class="card card--front" aria-label="Card front">
    <div class="brand">
      <div class="brand__illustration" role="img" aria-label="Mascot illustration holding a bunch of party balloons"></div>
      <p class="brand__name">Quandong Celebration Crafters</p>
    </div>

    <div class="name-band">Rosalind</div>

    <ul class="contact">
      <li class="contact__item contact__item--phone">
        <svg class="contact__icon" viewBox="0 0 20 20" aria-hidden="true">
          <path d="M2 6c0-2 3-3 8-3s8 1 8 3v2h-4V6H6v2H2z" fill="#fff"/>
          <rect x="4" y="9" width="12" height="8" rx="1" fill="#fff"/>
        </svg>
        <span>0417365920</span>
      </li>
      <li class="contact__item contact__item--email">
        <svg class="contact__icon" viewBox="0 0 20 20" aria-hidden="true">
          <rect x="2" y="4" width="16" height="12" fill="none" stroke="#fff" stroke-width="1.8"/>
          <path d="M2 4l8 7 8-7" fill="none" stroke="#fff" stroke-width="1.8"/>
        </svg>
        <span>ros@quandongfetes.com.au</span>
      </li>
      <li class="contact__item contact__item--web">
        <svg class="contact__icon" viewBox="0 0 20 20" aria-hidden="true">
          <path d="M8 12l4-4M7 9L4.5 11.5a2.5 2.5 0 003.5 3.5L10.5 12.5M13 11l2.5-2.5A2.5 2.5 0 0012 5L9.5 7.5" fill="none" stroke="#fff" stroke-width="1.8" stroke-linecap="round"/>
        </svg>
        <span>www.quandongfetes.com.au</span>
      </li>
    </ul>

    <div class="strip" aria-hidden="true">
      <span class="s-yellow"></span><span class="s-magenta"></span><span class="s-cyan"></span><span class="s-purple"></span>
    </div>
  </section>

  <section class="card card--back" aria-label="Card back">
    <div class="services">
      <div class="service">
        <span class="service__tag service__tag--yellow">business party planning</span>
        <span class="service__rule service__rule--inline" style="left:244px"></span>
        <span class="service__rule service__rule--full"></span>
      </div>
      <div class="service">
        <span class="service__tag service__tag--magenta">party hire</span>
        <span class="service__rule service__rule--inline" style="left:108px"></span>
        <span class="service__rule service__rule--full"></span>
      </div>
      <div class="service">
        <span class="service__tag service__tag--cyan">party supplies</span>
        <span class="service__rule service__rule--inline" style="left:142px"></span>
        <span class="service__rule service__rule--full"></span>
      </div>
    </div>
    <div class="appointment" aria-label="Appointment details">
      <div class="appointment__rule"></div>
      <div class="appointment__rule"></div>
    </div>
    <div class="strip" aria-hidden="true">
      <span class="s-yellow"></span><span class="s-magenta"></span><span class="s-cyan"></span><span class="s-purple"></span>
    </div>
  </section>

</main>
</body>
</html>
```